Letterhead

Create letterhead for corporate letters, proposals, thank yous, etc.

Target Market(s)

Technology, Communications

Industry/Entity Type

Information Technology

```html
<!DOCTYPE html>
<html lang="en">
<head>
<meta charset="utf-8">
<title>Nodeline Letterhead</title>
<link rel="stylesheet" href="https://fonts.googleapis.com/css2?family=Open+Sans:wght@300;400;700&display=swap">
<style>
  :root {
    --brand-blue: #1b7bbf;
    --paper: #ffffff;
    --ink-white: #ffffff;
    --brand-text: #4a5560;
    --faint-mark: #f1f3f5;
  }
  * { margin: 0; padding: 0; box-sizing: border-box; }
  html, body { width: 831px; height: 1200px; overflow: hidden; background: var(--paper); }
  .letterhead {
    position: relative;
    width: 831px;
    height: 1200px;
    background: var(--paper);
    font-family: "Open Sans", Arial, sans-serif;
    overflow: hidden;
  }
  .band { position: absolute; left: 0; width: 831px; display: block; }
  .band-top { top: 0; height: 160px; }
  .band-bottom { bottom: 0; height: 110px; }
  .band path { fill: var(--brand-blue); }

  .brand-name {
    position: absolute;
    left: 70px;
    top: 52px;
    font-size: 44px;
    font-weight: 300;
    color: var(--brand-text);
    letter-spacing: 0.5px;
    line-height: 1;
  }

  .contact-list {
    position: absolute;
    right: 52px;
    top: 52px;
    list-style: none;
    text-align: right;
  }
  .contact-list li {
    display: flex;
    justify-content: flex-end;
    align-items: center;
    gap: 14px;
    color: var(--ink-white);
    font-size: 13px;
    line-height: 22px;
  }
  .contact-list svg { width: 13px; height: 13px; flex: none; }
  .contact-list svg * { fill: var(--ink-white); }

  .background-mark {
    position: absolute;
    left: 0;
    top: 560px;
    width: 831px;
    text-align: center;
    font-size: 180px;
    font-weight: 300;
    color: var(--faint-mark);
    line-height: 1;
    user-select: none;
  }

  .address-block {
    position: absolute;
    left: 55px;
    top: 1140px;
    color: var(--ink-white);
    font-size: 12px;
    line-height: 18px;
  }
  .address-block .label { font-weight: 700; }
</style>
</head>
<body>
  <main class="letterhead">
    <svg class="band band-top" viewBox="0 0 831 160" preserveAspectRatio="none" aria-hidden="true">
      <path d="M140 0 C 260 70, 520 140, 831 125 L 831 0 Z"/>
    </svg>

    <div class="brand-name">Nodeline</div>

    <ul class="contact-list">
      <li>0400 555 018
        <svg viewBox="0 0 16 16" aria-hidden="true"><path d="M3.6 1.2l2.2 2.9-1.3 1.6c.8 1.9 2.2 3.3 4.1 4.2l1.6-1.3 2.9 2.2-1.2 2.6C6.7 13.2 2.8 9.3 1 3.1z"/></svg>
      </li>
      <li>info@nodelinetech.com
        <svg viewBox="0 0 16 16" aria-hidden="true"><path d="M1 3h14v1.2L8 9 1 4.2z"/><path d="M1 5.8L8 10.5l7-4.7V13H1z"/></svg>
      </li>
      <li>www.nodelinetech.com
        <svg viewBox="0 0 16 16" aria-hidden="true"><path d="M2 2h12v12H2zM3.5 5v7.5h9V5z"/></svg>
      </li>
    </ul>

    <div class="background-mark" aria-hidden="true">Nodeline</div>

    <svg class="band band-bottom" viewBox="0 0 831 110" preserveAspectRatio="none" aria-hidden="true">
      <path d="M0 10 C 260 -5, 560 45, 720 110 L 0 110 Z"/>
    </svg>

    <address class="address-block">
      <div class="label">Address</div>
      <div>Unit 4, 12 Harbour Lane, Westmere NSW 2100</div>
    </address>
  </main>
</body>
</html>
```